beauty salon

providing waxing services from a home base this must include which I will provide a price list and an address

Industry/Entity Type

Beauty Salon

Font styles to use
Script

Colors

Designer to choose colors to be used in the design.

```html
<!DOCTYPE html>
<html lang="en">
<head>
<meta charset="utf-8">
<title>Clara's Haven Salon – Price List</title>
<link rel="stylesheet" href="https://fonts.googleapis.com/css2?family=Cabin:wght@400;600;700&family=Kaushan+Script&family=Great+Vibes&family=Dancing+Script:wght@600&display=swap">
<style>
  :root {
    --purple: #6e2a8a;
    --purple-deep: #5e1f78;
    --plum-text: #7a2d8f;
    --teal: #1f8a72;
    --white: #ffffff;
    --neon: #eaf6ff;
    --neon-glow: #7fc8ff;
    --skin-a: #f3dccf;
    --skin-b: #e9c3b4;
    --petal: #f4d3ea;
  }
  * { margin: 0; padding: 0; box-sizing: border-box; }
  html, body { width: 853px; height: 1200px; overflow: hidden; background: var(--white); }
  .flyer { position: relative; width: 853px; height: 1200px; overflow: hidden; background: var(--white); font-family: "Cabin", sans-serif; }
  .panel { position: absolute; inset: 0; width: 853px; height: 1200px; }

  .brand { position: absolute; left: 22px; top: 92px; display: flex; align-items: center; gap: 10px; }
  .brand-dot { width: 18px; height: 18px; border-radius: 50%; background: var(--teal); }
  .brand-name { font-family: "Cabin", sans-serif; font-weight: 700; font-size: 29px; color: var(--plum-text); }

  .hero { position: absolute; left: 18px; top: 174px; width: 378px; height: 372px;
    background: radial-gradient(ellipse at 55% 45%, var(--skin-a) 0%, var(--skin-b) 45%, rgba(255,255,255,0) 75%),
                radial-gradient(circle at 45% 70%, var(--petal) 0%, rgba(255,255,255,0) 40%); }

  .info { position: absolute; font-family: "Kaushan Script", cursive; font-size: 27px; line-height: 40px; }
  .therapist { left: 20px; top: 568px; width: 380px; text-align: center; color: var(--plum-text); }
  .mobile { left: 26px; top: 724px; color: var(--teal); }
  .address { left: 30px; top: 808px; color: var(--plum-text); }
  .address .label, .hours .label, .mobile .label { color: var(--teal); }
  .address .line2 { padding-left: 124px; display: block; }
  .hours { left: 20px; top: 914px; color: var(--plum-text); }
  .hours .row { display: block; padding-left: 155px; }
  .hours .row:first-child { padding-left: 0; }
  .offer { position: absolute; left: 40px; top: 1090px; font-family: "Kaushan Script", cursive; font-size: 27px; color: var(--teal); transform: rotate(-13deg); transform-origin: left center; white-space: nowrap; }

  .price-title { position: absolute; left: 405px; top: 54px; font-family: "Dancing Script", cursive; font-weight: 600; font-size: 56px; color: var(--neon);
    transform: rotate(-18deg); text-shadow: 0 0 6px var(--neon-glow), 0 0 14px var(--neon-glow); }

  .menu { position: absolute; left: 540px; width: 280px; color: var(--white); }
  .menu-head { display: flex; align-items: center; gap: 14px; font-family: "Great Vibes", cursive; font-size: 30px; height: 40px; margin-left: 30px; }
  .menu-head .bullet { width: 22px; height: 22px; border-radius: 50%; background: var(--white); }
  .item { display: flex; justify-content: space-between; font-size: 23px; height: 36px; line-height: 36px; }
  .item .price { width: 48px; text-align: left; }
  .lady { top: 90px; }
  .eye { top: 698px; }
  .men { top: 842px; }
</style>
</head>
<body>
<div class="flyer">
  <svg class="panel" viewBox="0 0 853 1200" aria-hidden="true">
    <path d="M440 0 C 400 280, 520 430, 490 700 C 470 880, 520 1050, 505 1200 L 853 1200 L 853 0 Z" fill="var(--purple)"/>
    <path d="M560 678 Q 690 660 820 668" stroke="var(--white)" stroke-width="1.5" fill="none" opacity="0.8"/>
    <path d="M530 828 Q 680 812 830 822" stroke="var(--white)" stroke-width="1.5" fill="none" opacity="0.8"/>
  </svg>

  <div class="brand"><span class="brand-dot"></span><span class="brand-name">Clara's Haven Salon</span></div>

  <div class="hero" role="img" aria-label="Photo of a relaxed woman holding a pink lily flower near her shoulder"></div>

  <div class="info therapist">Beauty Therapist: Clara<br>Diploma of Beauty Therapy<br>at Marlowe College</div>
  <div class="info mobile"><span class="label">Mobile: 0400 555 019</span></div>
  <div class="info address"><span class="label">Address:</span> 12 Heron Lane<span class="line2">Riverside</span></div>
  <div class="info hours">
    <span class="row"><span class="label">Now Open:</span> Wednesday 10am – 4pm</span>
    <span class="row">Fridays 10am-7pm</span>
    <span class="row">Saturday 10am -4pm</span>
  </div>
  <div class="offer">-10% discount on first treatment.</div>

  <div class="price-title">Price List</div>

  <section class="menu lady">
    <h2 class="menu-head"><span class="bullet"></span>Lady's Waxing</h2>
    <div class="item"><span>Eyebrow</span><span class="price">$8</span></div>
    <div class="item"><span>Upper lip</span><span class="price">$8</span></div>
    <div class="item"><span>Chin</span><span class="price">$8</span></div>
    <div class="item"><span>Face wax</span><span class="price">$25</span></div>
    <div class="item"><span>Bikini line</span><span class="price">$15</span></div>
    <div class="item"><span>G string</span><span class="price">$20</span></div>
    <div class="item"><span>½ Brazilian</span><span class="price">$30</span></div>
    <div class="item"><span>Full Brazilian</span><span class="price">$40</span></div>
    <div class="item"><span>Half arm</span><span class="price">$20</span></div>
    <div class="item"><span>Upper half arm</span><span class="price">$20</span></div>
    <div class="item"><span>Full arm</span><span class="price">$25</span></div>
    <div class="item"><span>Half leg</span><span class="price">$15</span></div>
    <div class="item"><span>Upper leg</span><span class="price">$20</span></div>
    <div class="item"><span>¾ Leg</span><span class="price">$25</span></div>
    <div class="item"><span>Full leg</span><span class="price">$35</span></div>
  </section>

  <section class="menu eye">
    <h2 class="menu-head"><span class="bullet"></span>Eye Enhancement</h2>
    <div class="item"><span>Eyebrow tint</span><span class="price">$12</span></div>
    <div class="item"><span>Eyelash tint</span><span class="price">$15</span></div>
  </section>

  <section class="menu men">
    <h2 class="menu-head"><span class="bullet"></span>Men's Waxing</h2>
    <div class="item"><span>Eyebrow</span><span class="price">$10</span></div>
    <div class="item"><span>Half arm</span><span class="price">$20</span></div>
    <div class="item"><span>Upper half arm</span><span class="price">$25</span></div>
    <div class="item"><span>Full arm</span><span class="price">$30</span></div>
    <div class="item"><span>Half leg</span><span class="price">$25</span></div>
    <div class="item"><span>Full leg</span><span class="price">$45</span></div>
    <div class="item"><span>Chest wax</span><span class="price">$40</span></div>
    <div class="item"><span>Back wax</span><span class="price">$35</span></div>
  </section>
</div>
</body>
</html>
```